Website for legal expungement services with button to qualify/disqualify potential clients

Larkfield Record Relief, LLC is a law firm focusing in legal expungement servcies (allowing people to erase criminal court records, police records, proseution files, etc). I want a more modern look which exudes confidence in the services. I am looking for a clean website that looks very polished. I want to keep the pages to a minimum, as I want the page not so much to answer questions, but to direct traffic to contact the law office. I would like the main focus point to be an button which would take a client through a series of questions to see if they would qualify for the services; this serves two purposes 1) to collect contact info for future marketing via email and 2) eliminate individuals who we are currently unable to help. A current theme that I have played around with are "Change so much, you'll need to reintroduce yourself" alongside a picture of a guys hand outstretched.
On the landing page, I would like a very brief and to the point explanation of what the service would be (i.e. "Leave your past in the past; expunge all your criminal records" ), followed by a list of benefits that it provides. (NB: included is a file "law post card-02" that includes the main benefits to expungement). Also included are two logo files for a more updated logo I currently use ("LRR Logo" and LRR Logo2") (NB: I'm open to revisions on this as well). Lastly, I've had two very minor 'ads' that I did ("postcard back" and "HVC Ad") that I like the idea of.

Target Market(s)

Middle/upper-middle class, mostly male, people with a criminal record or criminal accusation

Industry/Entity Type

Legal Services

Coding

Coded - Design and coding required

Requirements
Must have
• Button that attracts attention up front (possibly stand out coloring) to click to open up a series of questions to qualify/eliminate prospects, and simultaneously gather their info. Also, must be mobile friendly.

```html
<!DOCTYPE html>
<html lang="en">
<head>
<meta charset="utf-8">
<title>Larkfield Record Relief</title>
<link href="https://fonts.googleapis.com/css2?family=Tinos:wght@400;700&family=Noto+Sans:wght@300;400&display=swap" rel="stylesheet">
<style>
:root{
  --navy:#12427a;
  --navy-deep:#0f3a6c;
  --ink:#1c1c1c;
  --white:#ffffff;
  --black:#000000;
  --serif:"Tinos", "Times New Roman", serif;
  --sans:"Noto Sans", Arial, sans-serif;
}
*{margin:0;padding:0;box-sizing:border-box}
html,body{width:1200px;height:3792px;overflow:hidden;background:var(--white)}
body{position:relative;font-family:var(--sans);color:var(--ink)}
.abs{position:absolute}
.brand-square{border:2px solid var(--navy);width:34px;height:34px}
.tag{position:absolute;border:3px solid var(--navy);display:flex;align-items:center;justify-content:center;font-family:var(--serif);font-weight:700;font-size:22px;color:var(--navy)}
.tag.light{border-color:var(--white);background:var(--white)}
.divider{position:absolute;width:2px;background:var(--navy)}
.divider.light{background:var(--white)}
.section-title{position:absolute;font-family:var(--serif);font-weight:700;font-size:30px;color:var(--navy);letter-spacing:.3px}
.section-title.light{color:var(--white)}

/* header */
.site-header{position:absolute;left:0;top:0;width:1200px;height:85px;background:var(--white)}
.header-brand{position:absolute;left:99px;top:25px;display:flex;align-items:center;gap:18px}
.header-brand .name{font-family:var(--serif);font-size:16px;line-height:18px;color:var(--navy);letter-spacing:1px}
.header-rule{position:absolute;left:220px;top:8px;width:2px;height:70px;background:var(--navy)}
.nav a{position:absolute;top:33px;font-family:var(--serif);font-size:15px;color:var(--ink);text-decoration:none}
.nav a.current{color:var(--navy);text-decoration:underline}
.btn{position:absolute;display:flex;align-items:center;justify-content:center;font-family:var(--serif);font-weight:700;text-decoration:none}
.btn-outline{border:3px solid var(--navy);color:var(--ink);background:var(--white)}

/* hero */
.hero{position:absolute;left:0;top:85px;width:1200px;height:600px;
  background:linear-gradient(90deg,#2a2416 0%,#3b3a22 25%,#4f5a2c 45%,#8a7a5e 62%,#b99a80 72%,#8e8a86 85%,#9ea3a8 100%)}
.hero h1{position:absolute;left:97px;top:168px;width:600px;font-family:var(--serif);font-weight:700;font-size:52px;line-height:60px;color:var(--white)}
.hero .btn{left:97px;top:371px;width:196px;height:50px;border:3px solid var(--white);color:var(--white);font-size:16px}

/* qualify */
.photo-frame{position:absolute;border:3px solid var(--navy);background:var(--white)}
.photo{position:absolute}
.case-list .item{position:absolute;left:587px;display:flex;align-items:center;gap:12px;font-size:20px;color:var(--ink);line-height:30px}
.case-list .icon{width:77px;height:53px;background:var(--navy);flex:none;display:flex;align-items:center;justify-content:center}

/* benefits */
.benefits{position:absolute;left:0;top:1217px;width:1200px;height:772px;
  background:linear-gradient(180deg,rgba(20,70,125,.94),rgba(18,66,120,.96)),linear-gradient(90deg,#3a4f6a,#24476f)}
.benefits .lead{position:absolute;left:140px;top:176px;width:920px;text-align:center;font-size:15.5px;line-height:31px;color:#e6edf6;font-weight:300}
.benefit{position:absolute;width:240px;text-align:center;color:var(--white);font-size:15px;line-height:31px;font-weight:300}
.benefit svg{display:block;margin:0 auto 8px}

/* records */
.checks .row{position:absolute;left:99px;display:flex;align-items:center;gap:12px;font-size:17px;color:#2b2b2b}

/* services */
.services{position:absolute;left:0;top:2526px;width:1200px;height:646px;
  background:linear-gradient(180deg,rgba(22,72,128,.95),rgba(17,64,118,.97)),linear-gradient(90deg,#33445a,#1e4370)}
.card{position:absolute;top:175px;width:454px;height:400px;background:var(--white)}
.card .photo{left:0;top:0;width:454px;height:259px}
.card .btn{left:22px;top:287px;width:411px;height:81px;font-size:21px}

/* cta */
.cta p{position:absolute;left:0;top:3226px;width:1200px;text-align:center;font-family:var(--serif);font-size:30px;line-height:44px;color:var(--ink)}
.cta strong{color:var(--navy)}

/* footer */
.site-footer{position:absolute;left:0;top:3450px;width:1200px;height:342px;background:var(--black);color:var(--white)}
.footer-links a{position:absolute;top:204px;transform:translateX(-50%);font-family:var(--serif);font-size:15px;color:var(--white);text-decoration:none;white-space:nowrap}
.copyright{position:absolute;left:0;top:255px;width:1200px;text-align:center;font-family:var(--serif);font-size:14px}
</style>
</head>
<body>

<header class="site-header">
  <div class="header-brand">
    <div class="brand-square"></div>
    <div style="width:80px"></div>
    <div class="name">LARKFIELD RECORD<br>RELIEF</div>
  </div>
  <div class="header-rule"></div>
  <nav class="nav">
    <a class="current" style="left:568px" href="#">Home</a>
    <a style="left:659px" href="#">About Us</a>
    <a style="left:771px" href="#">Services</a>
    <a style="left:877px" href="#">Benefits</a>
  </nav>
  <a class="btn btn-outline" style="left:964px;top:18px;width:134px;height:50px;font-size:15px" href="#">Contact Us</a>
</header>

<section class="hero" role="img" aria-label="Photo of a man's hand outstretched in greeting against a blurred green background">
  <h1>Change so much,you'll need to reintroduce yourself</h1>
  <a class="btn" href="#">Book An Appointment</a>
</section>

<section class="qualify">
  <div class="photo-frame" style="left:99px;top:762px;width:451px;height:393px"></div>
  <div class="photo" style="left:110px;top:772px;width:429px;height:373px;background:linear-gradient(135deg,#9aa3ab,#6c6f70 45%,#4b5a6e 70%,#c8ccd0)" role="img" aria-label="Photo of two businessmen shaking hands in an office"></div>

  <div class="tag" style="left:587px;top:814px;width:95px;height:49px">LRR</div>
  <div class="divider" style="left:700px;top:795px;height:86px"></div>
  <h2 class="section-title" style="left:717px;top:821px;font-size:29px">What types of cases qualify:</h2>

  <div class="case-list">
    <div class="item" style="top:903px"><span class="icon"><svg width="34" height="34" viewBox="0 0 34 34" fill="none" stroke="#fff" stroke-width="1.6"><circle cx="17" cy="9" r="6"/><path d="M6 32v-8h8v8M20 32v-8h8v8M17 15v9"/></svg></span>Criminal accusations that were dismissed</div>
    <div class="item" style="top:983px"><span class="icon"><svg width="34" height="34" viewBox="0 0 34 34" fill="none" stroke="#fff" stroke-width="1.6"><rect x="7" y="4" width="20" height="26"/><circle cx="17" cy="14" r="4"/><path d="M11 24h12M11 27h8"/></svg></span>Criminal cases that went into a diversionary<br>program</div>
    <div class="item" style="top:1067px"><span class="icon"><svg width="38" height="34" viewBox="0 0 38 34" fill="none" stroke="#fff" stroke-width="1.6"><circle cx="10" cy="22" r="7"/><circle cx="27" cy="11" r="7"/><path d="M15 17l7-2"/></svg></span>Convictions</div>
  </div>
</section>

<section class="benefits" role="region" aria-label="Benefits">
  <div class="tag light" style="left:330px;top:90px;width:94px;height:52px">LRR</div>
  <div class="divider light" style="left:442px;top:30px;height:86px"></div>
  <h2 class="section-title light" style="left:459px;top:88px">The Benefits of Expungement</h2>
  <p class="lead">Larkfield Record Relief is 5-star rated firm, which has been formed with the passing of the New Mexico Expungement law of 2020. It is a subdivision of the Harlow Law Group, and since its creation has helped over 100 New Mexican citizens successfully expunge their criminal records.</p>

  <div class="benefit" style="left:101px;top:292px"><svg width="118" height="118" viewBox="0 0 118 118"><circle cx="59" cy="59" r="55" fill="var(--navy)" stroke="#fff" stroke-width="7"/><g fill="none" stroke="#fff" stroke-width="2"><path d="M35 80h14V70H35zM52 80h14V62H52zM69 80h14V54H69z"/><path d="M36 55l18-12 10 6 18-16M74 33h8v8"/><circle cx="44" cy="40" r="8"/></g></svg>More and better job opportunities leading to higher income</div>
  <div class="benefit" style="left:357px;top:292px"><svg width="118" height="118" viewBox="0 0 118 118"><circle cx="59" cy="59" r="55" fill="var(--navy)" stroke="#fff" stroke-width="7"/><g fill="none" stroke="#fff" stroke-width="2"><path d="M59 30L40 50h10v32h18V50h10z"/><path d="M52 72l14-14"/><circle cx="53" cy="59" r="3"/><circle cx="65" cy="71" r="3"/></g></svg>Loan qualification and better loan rates</div>
  <div class="benefit" style="left:613px;top:292px"><svg width="118" height="118" viewBox="0 0 118 118"><circle cx="59" cy="59" r="55" fill="var(--navy)" stroke="#fff" stroke-width="7"/><g fill="none" stroke="#fff" stroke-width="2"><path d="M59 32l22 8v16c0 14-10 24-22 30-12-6-22-16-22-30V40z"/><rect x="51" y="56" width="16" height="12"/><path d="M54 56v-5a5 5 0 0110 0v5"/></g></svg>Protecting your privacy</div>
  <div class="benefit" style="left:868px;top:292px"><svg width="118" height="118" viewBox="0 0 118 118"><circle cx="59" cy="59" r="55" fill="var(--navy)" stroke="#fff" stroke-width="7"/><g fill="none" stroke="#fff" stroke-width="2"><path d="M40 42l20-9 20 9-20 9z"/><path d="M48 46v9c8 5 16 5 24 0v-9"/><path d="M36 72c8-6 16-6 22-2h12c4 0 4 6 0 6H58M36 82l10-4 18 3 16-10"/></g></svg>Better education opportunities</div>

  <div class="benefit" style="left:101px;top:512px"><svg width="118" height="118" viewBox="0 0 118 118"><circle cx="59" cy="59" r="55" fill="var(--navy)" stroke="#fff" stroke-width="7"/><g fill="none" stroke="#fff" stroke-width="2"><rect x="40" y="32" width="34" height="48"/><circle cx="57" cy="50" r="7"/><path d="M47 66h20M47 72h14M70 70l14-30 4 2-14 30z"/></g></svg>Removing the stigma of having a criminal record</div>
  <div class="benefit" style="left:357px;top:512px"><svg width="118" height="118" viewBox="0 0 118 118"><circle cx="59" cy="59" r="55" fill="var(--navy)" stroke="#fff" stroke-width="7"/><g fill="none" stroke="#fff" stroke-width="2"><path d="M36 56l23-18 23 18M41 52v28h36V52"/><rect x="53" y="64" width="12" height="16"/><path d="M46 58h8v6h-8zM64 58h8v6h-8z"/></g></svg>More options for housing</div>
  <div class="benefit" style="left:613px;top:512px"><svg width="118" height="118" viewBox="0 0 118 118"><circle cx="59" cy="59" r="55" fill="var(--navy)" stroke="#fff" stroke-width="7"/><g fill="none" stroke="#fff" stroke-width="2"><rect x="34" y="36" width="44" height="34"/><path d="M34 44h44M46 56l-4 4 4 4M56 56l4 4-4 4"/><circle cx="74" cy="70" r="8"/><circle cx="74" cy="70" r="3"/></g></svg>Qualifying for government assistance programs</div>
  <div class="benefit" style="left:868px;top:512px"><svg width="118" height="118" viewBox="0 0 118 118"><circle cx="59" cy="59" r="55" fill="var(--navy)" stroke="#fff" stroke-width="7"/><g fill="none" stroke="#fff" stroke-width="2"><rect x="40" y="34" width="32" height="48"/><rect x="50" y="30" width="12" height="7"/><path d="M46 46h4M54 46h12M46 56h4M54 56h12M46 66h4M54 66h8"/><path d="M70 60l12 4v8c0 6-6 10-12 12-6-2-12-6-12-12v-8z"/><path d="M65 72l4 4 7-7"/></g></svg>Lower insurance premiums</div>
</section>

<section class="records">
  <div class="tag" style="left:99px;top:2109px;width:94px;height:51px">LRR</div>
  <div class="divider" style="left:212px;top:2093px;height:84px"></div>
  <h2 class="section-title" style="left:228px;top:2095px;font-size:29px;line-height:38px">How your records are seen<br>by the public:</h2>
  <div class="checks">
    <div class="row" style="top:2205px"><svg width="20" height="20" viewBox="0 0 20 20"><rect width="20" height="20" rx="3" fill="var(--navy)"/><path d="M5 10l3.5 3.5L15 7" fill="none" stroke="#fff" stroke-width="2.2"/></svg>Public reporting (www.statecourtsportal.org)</div>
    <div class="row" style="top:2250px"><svg width="20" height="20" viewBox="0 0 20 20"><rect width="20" height="20" rx="3" fill="var(--navy)"/><path d="M5 10l3.5 3.5L15 7" fill="none" stroke="#fff" stroke-width="2.2"/></svg>Police reports</div>
    <div class="row" style="top:2295px"><svg width="20" height="20" viewBox="0 0 20 20"><rect width="20" height="20" rx="3" fill="var(--navy)"/><path d="M5 10l3.5 3.5L15 7" fill="none" stroke="#fff" stroke-width="2.2"/></svg>State Department of Public Safety</div>
    <div class="row" style="top:2340px"><svg width="20" height="20" viewBox="0 0 20 20"><rect width="20" height="20" rx="3" fill="var(--navy)"/><path d="M5 10l3.5 3.5L15 7" fill="none" stroke="#fff" stroke-width="2.2"/></svg>District attorney prosecution files</div>
    <div class="row" style="top:2385px"><svg width="20" height="20" viewBox="0 0 20 20"><rect width="20" height="20" rx="3" fill="var(--navy)"/><path d="M5 10l3.5 3.5L15 7" fill="none" stroke="#fff" stroke-width="2.2"/></svg>Court records</div>
  </div>
  <div class="photo-frame" style="left:624px;top:2063px;width:474px;height:385px;border-width:0 3px 3px 3px"></div>
  <div class="photo" style="left:636px;top:2058px;width:466px;height:379px;background:linear-gradient(135deg,#6d6a66,#b59a72 40%,#d9c6a8 60%,#7b6f63)" role="img" aria-label="Overhead photo of a team meeting around a wooden table with laptops and papers"></div>
</section>

<section class="services">
  <div class="tag light" style="left:445px;top:75px;width:94px;height:50px">LRR</div>
  <div class="divider light" style="left:557px;top:56px;height:86px"></div>
  <h2 class="section-title light" style="left:577px;top:85px">Our Services</h2>
  <div class="card" style="left:134px">
    <div class="photo" style="background:linear-gradient(135deg,#f1f1f0,#d9d6d2 45%,#8a8c90 70%,#e9e7e4)" role="img" aria-label="Photo of a smiling business team shaking hands around a laptop"></div>
    <a class="btn btn-outline" href="#">Leave your past in the past</a>
  </div>
  <div class="card" style="left:611px">
    <div class="photo" style="background:linear-gradient(135deg,#3d4652,#6e7680 40%,#c9b39b 65%,#5b6572)" role="img" aria-label="Photo of a man and woman discussing work at a desk"></div>
    <a class="btn btn-outline" href="#">Expunge all your criminal records</a>
  </div>
</section>

<section class="cta">
  <p>To see if you qualify for expungement or for additional<br>information, contact us <strong>555-014-2290</strong></p>
  <a class="btn btn-outline" style="left:531px;top:3338px;width:136px;height:49px;font-size:16px" href="#">Contact Us</a>
</section>

<footer class="site-footer">
  <div class="abs" style="left:430px;top:94px;width:56px;height:56px;border:3px solid var(--white)"></div>
  <div class="abs" style="left:563px;top:65px;width:2px;height:106px;background:var(--white)"></div>
  <div class="abs" style="left:609px;top:90px;font-family:var(--serif);font-size:25px;line-height:30px;letter-spacing:1.5px">LARKFIELD RECORD<br>RELIEF</div>
  <nav class="footer-links">
    <a style="left:231px" href="#">Home</a>
    <a style="left:325px" href="#">About Us</a>
    <a style="left:427px" href="#">Services</a>
    <a style="left:525px" href="#">Benefits</a>
    <a style="left:631px" href="#">Contact Us</a>
    <a style="left:757px" href="#">Privacy Policy</a>
    <a style="left:920px" href="#">Terms and Conditions</a>
  </nav>
  <p class="copyright">Copyrights@2023.Larkfield Record Relief.All Rights Reserved</p>
</footer>

</body>
</html>
```